Tandle Repair - Handyman and Home Repair Services

I need a business card/letterhead logo for my new handyman service in my local area. I'm happy for a logo design to be done prior to business card design so it can be incorporated on to the card, for which I'd be happy to pay more for. I'd like it to be modern and not using the typical pictures of tools and cartoon characters in dungarees! I like the idea of tools but in a more modern way i.e subtle background images in different shades to main colour. I do like the american retro designs and those that show age and patina for example, having an image half old, half new in its appearance to represent the repairing of things. Colours in mind are 1950's retro colours, ie using grey with pastel greens, red and cream. I'd like to break the mould and the stigma thats attached to these jobs and make it more cool and up to date. I hope this will attract interior designers and more modern businesses to use my services.

This is the logo design I like and would be happy for this idea and colours:

http://toast-a-roam.co.uk/wp-content/uploads/2011/01/t-r_logo600px.png

```html
<!DOCTYPE html>
<html lang="en">
<head>
<meta charset="utf-8">
<title>Tandle Repair – Business Card</title>
<link rel="stylesheet" href="https://fonts.googleapis.com/css2?family=Arimo:wght@400;700&display=swap">
<style>
  :root {
    --page-bg: #e9ebee;
    --card-white: #ffffff;
    --card-shade: #f1f2f4;
    --divider-grey: #a9abb0;
    --blue-light: #8fd2f4;
    --blue-mid: #4fb4e6;
    --blue-deep: #2a9fdc;
    --brand-blue: #2f9fe0;
    --tagline-grey: #6b6f76;
    --text-white: #ffffff;
  }
  * { margin: 0; padding: 0; box-sizing: border-box; }
  html, body {
    width: 1200px; height: 901px; overflow: hidden;
    background: var(--page-bg);
    font-family: "Arimo", Arial, sans-serif;
  }
  .business-card {
    position: absolute; left: 110px; top: 170px;
    width: 980px; height: 560px;
    border-radius: 60px; overflow: hidden;
    background: radial-gradient(ellipse at 58% 48%, var(--blue-light) 0%, var(--blue-mid) 45%, var(--blue-deep) 100%);
    box-shadow: 0 18px 40px rgba(40, 50, 70, 0.18);
  }
  .card-curve { position: absolute; inset: 0; width: 100%; height: 100%; }
  .brand {
    position: absolute; left: 90px; top: 205px; width: 320px;
    text-align: center;
  }
  .brand-mark {
    display: inline-block; width: 22px; height: 22px;
    background: var(--brand-blue); margin-bottom: 16px;
  }
  .brand-name {
    font-weight: 700; font-size: 50px; line-height: 1;
    color: var(--brand-blue); letter-spacing: 0.5px;
  }
  .brand-tagline {
    margin-top: 10px; font-size: 15px; color: var(--tagline-grey);
  }
  .contact-block {
    position: absolute; right: 52px; top: 50px;
    text-align: right; color: var(--text-white);
  }
  .person-name { font-weight: 700; font-size: 40px; line-height: 1.15; }
  .person-title { font-size: 28px; line-height: 1.2; }
  .address { margin-top: 46px; font-size: 26px; line-height: 1.3; }
  .contact-list { margin-top: 48px; list-style: none; font-size: 24px; line-height: 1.4; }
  .contact-list li { display: flex; justify-content: flex-end; align-items: center; gap: 10px; }
  .contact-icon { width: 20px; height: 20px; fill: var(--text-white); stroke: var(--text-white); }
</style>
</head>
<body>
  <section class="business-card">
    <svg class="card-curve" viewBox="0 0 980 560" preserveAspectRatio="none" aria-hidden="true">
      <path fill="var(--divider-grey)" d="M0,0 H505 C455,40 432,125 452,225 C472,335 410,462 185,560 H0 Z"/>
      <defs>
        <linearGradient id="whitePanel" x1="0" y1="0" x2="1" y2="1">
          <stop offset="0" stop-color="var(--card-white)"/>
          <stop offset="1" stop-color="var(--card-shade)"/>
        </linearGradient>
      </defs>
      <path fill="url(#whitePanel)" d="M0,0 H480 C430,40 408,122 428,222 C448,332 388,458 160,560 H0 Z"/>
    </svg>

    <div class="brand">
      <span class="brand-mark"></span>
      <div class="brand-name">Tandle Repair</div>
      <div class="brand-tagline">Handyman and Home Repair Services</div>
    </div>

    <div class="contact-block">
      <div class="person-name">Marcus Whitfield</div>
      <div class="person-title">Director General</div>
      <div class="address">Suite # 418, Elm<br>Bldg, NY 10452</div>
      <ul class="contact-list">
        <li>727510,248
          <svg class="contact-icon" viewBox="0 0 20 20" aria-hidden="true"><path stroke="none" d="M2 8c0-3 4-5 8-5s8 2 8 5l-3 1-1-2H6L5 9 2 8zM5 11h10l2 6H3l2-6z"/></svg>
        </li>
        <li>305-555-0148
          <svg class="contact-icon" viewBox="0 0 20 20" aria-hidden="true"><path stroke="none" d="M4 3h8v15H4zM13 8h4v10h-4z"/></svg>
        </li>
        <li>hello@tandlemail.com
          <svg class="contact-icon" viewBox="0 0 20 20" aria-hidden="true"><rect x="2" y="5" width="16" height="11" fill="none" stroke-width="2"/><path fill="none" stroke-width="2" d="M2 5l8 6 8-6"/></svg>
        </li>
        <li>www.tandlerepair.com
          <svg class="contact-icon" viewBox="0 0 20 20" aria-hidden="true"><g fill="none" stroke-width="1.6"><circle cx="10" cy="10" r="8"/><ellipse cx="10" cy="10" rx="3.5" ry="8"/><path d="M2 10h16M4 5.5h12M4 14.5h12"/></g></svg>
        </li>
      </ul>
    </div>
  </section>
</body>
</html>
```